Anzeigengestaltung für eine Hausarztpraxis
Zielgruppe
Wir sind eine Hausarztpraxis mit zwei Standorten und suchen eine Ärztin oder einen Arzt zur Anstellung in der klassischen Hausarzt Medizin am Standort Lindwil
Aufgabenstellung
Bitte beachtet den Text im Anhang, der ist schon vorgegeben. (Anzeigentext)
Wir suchen ein ruhiges, hochwertiges Layout für eine Stellenanzeige einer Hausarztpraxis in einem historischen Gebäude.
Der Text steht im Vordergrund, das Design soll zurückhaltend, klar und wertig sein.
Bitte keine Icons, keine bunten Farben, keine verspielten Elemente.
Gerne viel Weissraum, klare Typografie, ruhige Anmutung.
Schrift: Garamond für den Fliesstext (bereits gewählt).
Das Layout soll sowohl als PDF wie auch online funktionieren.
Optional: ein sehr dezentes grafisches Element oder eine ruhige Bildanmutung (z. B. Struktur, Licht, Architekturdetail).

```html
<!DOCTYPE html>
<html lang="de">
<head>
<meta charset="utf-8">
<title>Stellenanzeige Hausarztpraxis</title>
<link rel="stylesheet" href="https://fonts.googleapis.com/css2?family=Archivo:ital,wdth,wght@0,100..125,400..800;1,100..125,400..800&family=EB+Garamond:ital,wght@0,400..700;1,400..700&display=swap">
<style>
  :root {
    --backdrop: #eeeeee;
    --paper: #ffffff;
    --ink: #1d1d1d;
    --ink-soft: #2a2a2a;
    --slate: #4f6577;
    --slate-text: #56697c;
    --brand-green: #7ab51d;
    --sketch-light: #f3f3f3;
    --sketch-mid: #c9c9c9;
  }
  * { box-sizing: border-box; margin: 0; padding: 0; }
  html, body {
    width: 1200px; height: 800px; overflow: hidden;
    background: var(--backdrop);
  }
  .flyer {
    position: absolute; left: 330px; top: 18px;
    width: 540px; height: 764px;
    background: var(--paper);
    box-shadow: 0 4px 18px rgba(0,0,0,.12);
    font-family: "EB Garamond", Garamond, serif;
    color: var(--ink-soft);
    overflow: hidden;
  }
  .flyer__header { position: relative; height: 206px; }
  .brand {
    position: absolute; left: 44px; top: 46px;
    display: flex; align-items: center; gap: 8px;
    font-family: "Archivo", sans-serif; font-weight: 700;
    font-size: 14px; color: var(--ink);
  }
  .brand__dot { width: 9px; height: 9px; border-radius: 50%; background: var(--brand-green); }
  .house-visual {
    position: absolute; right: 0; top: 36px; width: 330px; height: 170px;
    background: radial-gradient(ellipse at 55% 45%, var(--sketch-mid) 0%, #e2e2e2 40%, var(--sketch-light) 68%, var(--paper) 90%);
  }
  .headline {
    position: absolute; left: 44px; top: 146px; width: 450px;
    font-family: "Archivo", sans-serif; font-stretch: 115%;
    font-weight: 800; font-size: 19px; line-height: 1.18; color: var(--ink);
  }
  .tagline {
    margin: 0 44px; padding-top: 6px;
    font-family: "Archivo", sans-serif; font-style: italic; font-size: 10px;
    color: var(--ink);
  }
  .body { padding: 16px 44px 0; font-size: 10.8px; line-height: 1.42; }
  .body p { margin-bottom: 6px; }
  .body h2 {
    font-weight: 500; font-size: 12.5px; color: var(--slate-text);
    margin-top: 10px; margin-bottom: 2px;
  }
  .contact {
    position: absolute; left: 44px; right: 44px; bottom: 46px;
    display: flex; align-items: flex-end; gap: 22px;
    font-size: 10.8px; line-height: 1.4;
  }
  .contact__invite { flex: 1; }
  .contact__invite strong { color: var(--ink); }
  .label { color: var(--slate-text); }
  .contact__divider { width: 1px; height: 62px; background: var(--slate); }
  .contact__address { width: 150px; font-size: 11px; font-style: normal; }
  .contact__address .practice { color: var(--slate-text); font-weight: 600; }
  .flyer__band {
    position: absolute; left: 0; right: 0; bottom: 0; height: 18px;
    background: var(--slate);
  }
</style>
</head>
<body>
<article class="flyer">
  <header class="flyer__header">
    <div class="brand"><span class="brand__dot"></span>Arztpraxis Lindenhof</div>
    <div class="house-visual" role="img" aria-label="Zarte Bleistiftzeichnung des historischen Praxisgebäudes mit Garten"></div>
    <h1 class="headline">Hausarztmedizin mit Tiefe – dort, wo man noch echte Grundversorgung lebt</h1>
  </header>
  <p class="tagline">Ein Ort, der trägt. Ein Team, das bleibt. Eine Arbeit, die Wertschätzung hat.</p>
  <section class="body">
    <p>Manche Orte verändern die Art, wie man arbeitet. Unsere Praxis in Lindwil ist so ein Ort.
    In einem historischen Gebäude gelegen, mit grosszügigem Ambiente, warmen Vertäfelungen und kunstvoller Wandbemalung, entstehen hier Behandlungsräume von Ruhe und Würde. Kein steriler Praxisalltag, sondern ein Ort, der Gespräche trägt und medizinische Arbeit unterstützt.</p>
    <p>Für diesen besonderen Ort suchen wir eine Hausärztin oder einen Hausarzt, die oder der nicht einfach einen Arbeitsplatz sucht, sondern einen Platz, an dem Medizin menschlich sein darf.</p>
    <h2>Ein Team mit Haltung</h2>
    <p>Sie arbeiten in einem freundlichen, über Jahre gewachsenen Team mit hoher personeller Kontinuität und geringer Fluktuation.</p>
    <h2>Zeit für gute Medizin</h2>
    <p>Unsere Patientinnen und Patienten sind überwiegend gut bis sehr gut situiert, wertschätzend und therapieoffen. Das ermöglicht ruhiges, strukturiertes Arbeiten mit Fokus auf Qualität, Beziehung und nachhaltige Behandlung.</p>
    <h2>Und sonst?</h2>
    <p>Der Praxisalltag ist klar strukturiert, ruhig und verlässlich. Geregelte und in Abstimmung flexible Arbeitszeiten ohne Wochenend- oder Nachtdienste, eine sehr gute leistungsbezogene Vergütung sowie ein respektvoller, wertschätzender Umgang auf Augenhöhe schaffen ein Umfeld, in dem man sich auf die medizinische Arbeit konzentrieren und langfristig wohlfühlen kann.</p>
  </section>
  <footer class="contact">
    <div class="contact__invite">
      <p>Wir freuen uns über eine unkomplizierte Kontaktaufnahme per <strong>E-Mail oder Telefon</strong> – gerne auch ganz unverbindlich und ohne vollständige Bewerbungsunterlagen.</p>
      <p><span class="label">E-Mail:</span> Melina.Korvath@arztpraxis-lindenhof.ch</p>
    </div>
    <div class="contact__divider"></div>
    <address class="contact__address">
      <div class="practice">Arztpraxis Lindenhof</div>
      Mühlegasse 7<br>
      4712 Lindwil<br>
      <span class="label">Tel:</span> 0620001122
    </address>
  </footer>
  <div class="flyer__band"></div>
</article>
</body>
</html>
```